KTR Associates Business Card

I would like to have a business card designed that uses my current logo and colors. I am not looking for anything to "out there" but can have a little fun so that it stands out.

I have a boutique consulting firm that specializes in strategic planning, change management, leadership development and innovation.

Industry/Entity Type

Leadership

Contact Information for Business Card

Marta Holloway
President
marta@ktr-associates-mail.com
919-555-0143

```html
<!DOCTYPE html>
<html lang="en">
<head>
<meta charset="utf-8">
<title>KTR Associates Business Card</title>
<link href="https://fonts.googleapis.com/css2?family=EB+Garamond:ital,wght@0,400;1,400&display=swap" rel="stylesheet">
<style>
  :root {
    --page: #ffffff;
    --card: #ffffff;
    --card-edge: #1e1e1e;
    --ink: #2b2622;
    --ink-soft: #4a4540;
    --skyline: #93bfa4;
    --accent-area: #e4efe8;
  }
  * { box-sizing: border-box; margin: 0; padding: 0; }
  html, body {
    width: 1200px;
    height: 750px;
    overflow: hidden;
    background: var(--page);
  }
  body {
    position: relative;
    font-family: "EB Garamond", Georgia, serif;
    font-variant-numeric: lining-nums;
    color: var(--ink);
  }
  .card {
    position: absolute;
    top: 206px;
    width: 471px;
    height: 268px;
    background: var(--card);
    border: 1.5px solid var(--card-edge);
    overflow: hidden;
  }
  .card--front { left: 133px; }
  .card--back { left: 626px; }

  .skyline {
    position: absolute;
    left: 0;
    right: 0;
    bottom: 0;
    height: 36px;
    background: var(--skyline);
  }

  .tagline {
    position: absolute;
    left: 0;
    right: 0;
    text-align: center;
    font-style: italic;
    font-size: 14px;
    line-height: 18px;
    color: var(--ink-soft);
    letter-spacing: 0.2px;
  }

  /* front */
  .brand-name {
    position: absolute;
    left: 0;
    right: 0;
    top: 62px;
    text-align: center;
    font-size: 48px;
    line-height: 1;
    color: var(--ink);
  }
  .card--front .tagline { top: 192px; }

  /* back */
  .card--back .tagline { top: 38px; }
  .accent-area {
    position: absolute;
    left: 39px;
    top: 66px;
    width: 385px;
    height: 18px;
    background: var(--accent-area);
  }
  .contact {
    position: absolute;
    left: 0;
    right: 0;
    top: 112px;
    text-align: center;
    font-size: 20px;
    line-height: 20.5px;
    letter-spacing: 1.2px;
    color: var(--ink);
  }
  .contact__email { font-size: 19px; letter-spacing: 0.8px; }
</style>
</head>
<body>
  <section class="card card--front">
    <div class="brand-name">KTR Associates</div>
    <p class="tagline">Strategic Planning · Management · Leadership</p>
    <div class="skyline" role="img" aria-label="Green city skyline silhouette"></div>
  </section>

  <section class="card card--back">
    <p class="tagline">Strategic Planning · Management · Leadership</p>
    <div class="accent-area" role="img" aria-label="Decorative green brush stroke"></div>
    <div class="contact">
      <div class="contact__name">Marta Holloway</div>
      <div class="contact__title">President</div>
      <div class="contact__email">marta@ktr-associates-mail.com</div>
      <div class="contact__phone">919-555-0143</div>
    </div>
    <div class="skyline" role="img" aria-label="Green city skyline silhouette"></div>
  </section>
</body>
</html>
```